Business Card for Orthopaedic Clinic.
Should have nice design, double sided that includes logo
Should include my name, my contact, my email, webpage. A QR code to scan business card.

please use dummy information for privacy reasons. I will provide my name, email, practice address once a winner is selected.

Target Market(s)

Future patients

Contact Information for Business Card

Name: Dr Ruk
Contact No: +65 90417263
Practice Address: Singapore
Email: doctor@brevlo.com
Website: www.brevlo.com

Colors
00a990

Requirements
Must have
• Logo and a nice colour scheme.
A QR Code for Contact Card.
Name
Contact
Practice Address
Email
Website.
Nice to have
• Nice colour scheme
Should not have
• Nothing too cluttered.

```html
<!DOCTYPE html>
<html lang="en">
<head>
<meta charset="utf-8">
<title>Stride Orthopaedics – Business Card</title>
<link href="https://fonts.googleapis.com/css2?family=Open+Sans:wght@400;600;700&display=swap" rel="stylesheet">
<style>
  :root {
    --backdrop: #4a4f50;
    --card: #14ab8f;
    --ink: #ffffff;
    --ink-soft: rgba(255, 255, 255, 0.85);
    --rule: rgba(255, 255, 255, 0.35);
  }
  * { box-sizing: border-box; margin: 0; padding: 0; }
  html, body {
    width: 1200px;
    height: 1050px;
    overflow: hidden;
    background: var(--backdrop);
    font-family: "Open Sans", Arial, sans-serif;
    color: var(--ink);
  }
  .sheet {
    position: relative;
    width: 1200px;
    height: 1050px;
  }
  .card {
    position: absolute;
    left: 200px;
    width: 800px;
    height: 457px;
    background: var(--card);
  }
  .card--back { top: 48px; }
  .card--front { top: 545px; }

  /* Wordmark */
  .wordmark {
    display: flex;
    align-items: center;
    gap: 18px;
    color: var(--ink);
    font-weight: 700;
    text-transform: uppercase;
    line-height: 1;
  }
  .wordmark__square {
    flex: none;
    background: var(--ink);
  }
  .wordmark__name {
    display: flex;
    flex-direction: column;
    gap: 6px;
  }

  /* Back side: details */
  .card--back .wordmark {
    position: absolute;
    left: 56px;
    top: 70px;
  }
  .card--back .wordmark__square { width: 54px; height: 54px; }
  .card--back .wordmark__name { font-size: 30px; letter-spacing: 1px; }
  .card--back .wordmark__name span:last-child { font-size: 20px; letter-spacing: 5px; }

  .practice-address {
    position: absolute;
    left: 56px;
    top: 300px;
    font-size: 15px;
    letter-spacing: 2px;
    text-transform: uppercase;
    color: var(--ink-soft);
    line-height: 1.45;
  }

  .contact {
    position: absolute;
    left: 420px;
    top: 222px;
    width: 340px;
  }
  .contact__name {
    font-size: 26px;
    font-weight: 700;
    letter-spacing: 2px;
    line-height: 1.2;
    margin-bottom: 4px;
  }
  .contact__title {
    font-size: 19px;
    font-weight: 700;
    letter-spacing: 3px;
    text-transform: uppercase;
    margin-bottom: 12px;
  }
  .contact__list { list-style: none; }
  .contact__item {
    display: flex;
    align-items: center;
    gap: 14px;
    font-size: 19px;
    letter-spacing: 2.5px;
    line-height: 32px;
  }
  .contact__icon {
    width: 22px;
    height: 22px;
    flex: none;
  }
  .contact__rule {
    margin-top: 14px;
    height: 1px;
    background: var(--rule);
    width: 360px;
    margin-left: -30px;
  }

  /* Front side: brand */
  .card--front .brand-block {
    position: absolute;
    inset: 0;
    display: flex;
    flex-direction: column;
    align-items: center;
    justify-content: center;
    gap: 40px;
  }
  .card--front .wordmark__square { width: 78px; height: 78px; }
  .card--front .wordmark__name { font-size: 46px; letter-spacing: 1.5px; }
  .card--front .wordmark__name span:last-child { font-size: 29px; letter-spacing: 7px; }
  .website-large {
    font-size: 28px;
    letter-spacing: 9px;
    text-transform: uppercase;
  }
  .qr-area {
    position: absolute;
    right: 40px;
    bottom: 40px;
    width: 86px;
    height: 86px;
    border: 2px solid var(--ink);
    background: rgba(255, 255, 255, 0.12);
  }
</style>
</head>
<body>
<main class="sheet">

  <section class="card card--back" aria-label="Card back: contact details">
    <div class="wordmark">
      <span class="wordmark__square" aria-hidden="true"></span>
      <span class="wordmark__name"><span>Stride</span><span>Orthopaedics</span></span>
    </div>

    <p class="practice-address">Practice Address<br>Singapore</p>

    <div class="contact">
      <p class="contact__name">Dr Ruk</p>
      <h2 class="contact__title">Orthopaedic Clinic</h2>
      <ul class="contact__list">
        <li class="contact__item">
          <svg class="contact__icon" viewBox="0 0 24 24" fill="none" stroke="#fff" stroke-width="1.8" aria-hidden="true">
            <rect x="6" y="2" width="12" height="20" rx="2"/>
            <rect x="8.5" y="5" width="7" height="5"/>
            <path d="M9 13h1M12 13h1M15 13h0.5M9 16h1M12 16h1M15 16h0.5M9 19h1M12 19h1M15 19h0.5"/>
          </svg>
          <span>+65 90417263</span>
        </li>
        <li class="contact__item">
          <svg class="contact__icon" viewBox="0 0 24 24" fill="none" stroke="#fff" stroke-width="1.8" aria-hidden="true">
            <rect x="2" y="5" width="20" height="14"/>
            <path d="M2 5l10 8 10-8M2 19l7.5-7M22 19l-7.5-7"/>
          </svg>
          <span>doctor@brevlo.com</span>
        </li>
        <li class="contact__item">
          <svg class="contact__icon" viewBox="0 0 24 24" fill="none" stroke="#fff" stroke-width="1.8" aria-hidden="true">
            <circle cx="12" cy="12" r="10"/>
            <ellipse cx="12" cy="12" rx="4.5" ry="10"/>
            <path d="M2 12h20M4 7h16M4 17h16"/>
          </svg>
          <span>www.brevlo.com</span>
        </li>
      </ul>
      <div class="contact__rule" aria-hidden="true"></div>
    </div>
  </section>

  <section class="card card--front" aria-label="Card front: brand">
    <div class="brand-block">
      <div class="wordmark">
        <span class="wordmark__square" aria-hidden="true"></span>
        <span class="wordmark__name"><span>Stride</span><span>Orthopaedics</span></span>
      </div>
      <p class="website-large">www.brevlo.com</p>
    </div>
    <div class="qr-area" role="img" aria-label="QR code for the contact card goes here"></div>
  </section>

</main>
</body>
</html>
```